Stationary for Home Builder
Larkfield Dwellings Inc.
Project: Stationary for Home Builder
Stationary for Home Builder - Construction
Creative Brief
Modern
Gaston Villemure
Owner
Suite 310-7816 62 Avenue Edmonton, AB T5K 3M2
gaston@larkfielddwellings.ca
larkfielddwellings.ca
The blue colour used in the logo should be replicated and used within the stationary / business cards. Feel free to use additional complementary colours as well (including, but not limited to the grey colour used in the logo).. The intention is to have a modern feel but remain professional. The backside of the card can have designs but should allow some space to write notes.

```html
<!DOCTYPE html>
<html lang="en">
<head>
<meta charset="utf-8">
<title>Larkfield Dwellings Inc. – Stationery</title>
<link href="https://fonts.googleapis.com/css2?family=Open+Sans:wght@400;600;800&display=swap" rel="stylesheet">
<style>
:root{
  --brand-blue:#1f6fc4;
  --brand-blue-dark:#0e4f9a;
  --brand-blue-light:#4f9ae6;
  --brand-grey:#6d7278;
  --paper:#ffffff;
  --rule:#c9ced4;
  --backdrop:#e9e6e2;
}
*{box-sizing:border-box;margin:0;padding:0}
html,body{width:1200px;height:458px;overflow:hidden}
body{background:var(--backdrop);font-family:"Open Sans",sans-serif;color:var(--brand-grey);position:relative}
.sheet{position:absolute;background:var(--paper);box-shadow:0 2px 6px rgba(0,0,0,.18)}
.brand{font-weight:800;color:var(--brand-blue);line-height:1;display:flex;align-items:center;gap:4px;letter-spacing:-.2px;white-space:nowrap}
.brand .mark{width:8px;height:8px;background:var(--brand-blue);flex:none}
.brand.on-blue{color:var(--paper)}
.brand.on-blue .mark{background:var(--paper)}
.tiny{font-size:4px;line-height:1.5;white-space:nowrap}

/* business card front */
.card-front{left:48px;top:132px;width:140px;height:84px}
.card-front .brand{position:absolute;left:10px;top:26px;font-size:8px}
.card-front .person{position:absolute;left:74px;top:12px}
.card-front .person b{display:block;font-size:5px;color:var(--brand-blue)}
.card-front .contact{position:absolute;left:74px;top:42px}
.card-front .stripe{position:absolute;left:0;right:0;bottom:0;height:5px;background:var(--brand-blue)}

/* business card back */
.card-back{left:48px;top:221px;width:140px;height:80px;background:linear-gradient(160deg,var(--brand-blue-light),var(--brand-blue) 55%,var(--brand-blue-dark));display:flex;flex-direction:column;align-items:center;justify-content:center;gap:8px}
.card-back .brand{font-size:9px}
.card-back .web{font-size:4px;color:#dbe9f8}

/* letterhead */
.letterhead{left:192px;top:36px;width:260px;height:389px}
.letterhead .brand{position:absolute;left:20px;top:22px;font-size:11px}
.letterhead .address{position:absolute;left:168px;top:18px}
.footer-band{position:absolute;left:0;right:0;bottom:0;height:16px;background:linear-gradient(90deg,var(--rule),var(--brand-blue));display:flex;align-items:center;justify-content:flex-end;padding-right:12px}
.footer-band span{font-size:5px;color:var(--paper);font-weight:600}

/* fax */
.fax{left:468px;top:36px;width:252px;height:389px}
.fax .brand{position:absolute;left:18px;top:22px;font-size:11px}
.fax .address{position:absolute;left:160px;top:18px}
.fax h2{position:absolute;right:20px;top:72px;font-size:10px;font-weight:800;color:var(--brand-grey)}
.fax-table{position:absolute;left:12px;right:12px;top:86px;height:68px;border:1px solid var(--brand-grey);padding:6px 8px}
.fax-fields{display:grid;grid-template-columns:1fr 1fr;grid-template-rows:repeat(3,12px);gap:2px 12px}
.fax-field{font-size:4px;border-bottom:1px solid var(--rule);display:flex;align-items:flex-end;padding-bottom:1px}
.fax-checks{display:flex;justify-content:space-between;margin-top:8px}
.fax-checks span{font-size:4px;display:flex;align-items:center;gap:3px;flex:none;white-space:nowrap}
.fax-checks i{width:4px;height:4px;border:1px solid var(--brand-grey);display:block;flex:none}

/* envelope back */
.envelope-back{left:732px;top:36px;width:415px;height:192px;overflow:hidden}
.envelope-back svg{position:absolute;inset:0}
.envelope-back .brand{position:absolute;left:50%;top:50px;transform:translateX(-50%);font-size:11px}

/* envelope front */
.envelope-front{left:732px;top:235px;width:415px;height:137px;overflow:hidden}
.envelope-front svg{position:absolute;inset:0}
.envelope-front .brand{position:absolute;right:56px;top:14px;font-size:11px}

/* small envelope */
.envelope-small{left:732px;top:307px;width:204px;height:120px;padding:18px}
.envelope-small .brand{font-size:11px}
.envelope-small .address{margin-top:12px}
</style>
</head>
<body>

<div class="sheet card-front">
  <div class="brand"><span class="mark"></span>Larkfield Dwellings</div>
  <div class="person tiny"><b>Gaston Villemure</b>Owner</div>
  <div class="contact tiny">T 780 555 0142<br>F 780 555 0143<br>gaston@larkfielddwellings.ca<br>Suite 310-7816 62 Avenue<br>Edmonton, AB T5K 3M2</div>
  <div class="stripe"></div>
</div>

<div class="sheet card-back">
  <div class="brand on-blue"><span class="mark"></span>Larkfield Dwellings</div>
  <div class="web">larkfielddwellings.ca</div>
</div>

<div class="sheet letterhead">
  <div class="brand"><span class="mark"></span>Larkfield Dwellings</div>
  <div class="address tiny">Suite 310-7816 62 Avenue<br>Edmonton, AB T5K 3M2<br>T 780 555 0142<br>F 780 555 0143</div>
  <div class="footer-band"><span>www.larkfielddwellings.ca</span></div>
</div>

<div class="sheet fax">
  <div class="brand"><span class="mark"></span>Larkfield Dwellings</div>
  <div class="address tiny">Suite 310-7816 62 Avenue<br>Edmonton, AB T5K 3M2<br>T 780 555 0142<br>F 780 555 0143</div>
  <h2>FAX</h2>
  <div class="fax-table">
    <div class="fax-fields">
      <div class="fax-field">TO:</div><div class="fax-field">FROM:</div>
      <div class="fax-field">FAX:</div><div class="fax-field">PAGES:</div>
      <div class="fax-field">PHONE:</div><div class="fax-field">DATE:</div>
    </div>
    <div class="fax-checks">
      <span><i></i>Urgent</span><span><i></i>For Review</span><span><i></i>Please comment</span><span><i></i>Please reply</span><span><i></i>Please recycle</span>
    </div>
  </div>
  <div class="footer-band"><span>www.larkfielddwellings.ca</span></div>
</div>

<div class="sheet envelope-back">
  <svg width="415" height="192" viewBox="0 0 415 192" aria-hidden="true">
    <path d="M0 0 L207 92 L415 0 Z" fill="#f4f6f8"/>
    <path d="M0 0 L207 95 L415 0" fill="none" stroke="var(--rule)" stroke-width="1"/>
  </svg>
  <div class="brand"><span class="mark"></span>Larkfield Dwellings</div>
</div>

<div class="sheet envelope-front">
  <svg width="415" height="137" viewBox="0 0 415 137" aria-hidden="true">
    <defs>
      <linearGradient id="envBand" x1="0" y1="0" x2="1" y2="0">
        <stop offset="0" stop-color="var(--brand-blue-light)"/>
        <stop offset="1" stop-color="var(--brand-blue-dark)"/>
      </linearGradient>
    </defs>
    <path d="M0 0 H415 V62 Q207 20 0 62 Z" fill="url(#envBand)"/>
  </svg>
  <div class="brand on-blue"><span class="mark"></span>Larkfield Dwellings</div>
</div>

<div class="sheet envelope-small">
  <div class="brand"><span class="mark"></span>Larkfield Dwellings</div>
  <div class="address tiny">Suite 310-7816 62 Avenue<br>Edmonton, AB T5K 3M2</div>
</div>

</body>
</html>
```